Design a Word Template and Powerpoint Template for a Venture Capital Fund

I'm looking to get a powerpoint template and word template designed ASAP under the same selected design. Its for a finance / Venture Capital business... keen to keep it clean but "pop" and stand up on its own as a strong brand, solid templates etc... Happy to talk. Thanks Kit

Target Market(s)

Venture Capital and Private Equity

Industry/Entity Type

Finance / Venture Capital / Management Consulting

Requirements
Nice to have
• Strong formatting, icons and optionality, images can be good too

```html
<!DOCTYPE html>
<html lang="en">
<head>
<meta charset="utf-8">
<title>Northfield Venture Partners – Stationery System</title>
<link href="https://fonts.googleapis.com/css2?family=Montserrat:wght@400;500&family=Open+Sans:wght@400;600&display=swap" rel="stylesheet">
<style>
:root{
  --board:#4a4a4a;
  --paper:#ffffff;
  --ink:#1a1a1a;
  --night:#000000;
  --charcoal:#1b1b1b;
  --mist:#f5f7f7;
  --rule:#8a8a8a;
  --ghost:#eeeeee;
  --sky-a:#0d3a66;
  --sky-b:#3b7fc0;
}
*{box-sizing:border-box;margin:0;padding:0}
html,body{width:1200px;height:1200px;overflow:hidden;background:var(--board)}
body{position:relative;font-family:"Open Sans",Arial,sans-serif;color:var(--ink)}
.page{position:absolute;width:245px;height:343px;background:var(--paper);overflow:hidden}
.page.dark{background:var(--night);color:#fff}
.c1{left:15px}.c2{left:321px}.c3{left:630px}.c4{left:939px}
.r1{top:33px}.r2{top:438px}.r3{top:840px}

.brand{position:absolute;display:flex;align-items:center;gap:4px;font-family:"Montserrat",Arial,sans-serif;font-weight:400;letter-spacing:.12em;white-space:nowrap}
.brand-square{display:block;width:6px;height:6px;background:currentColor}
.brand-name{font-size:6px;line-height:1}
.brand.lg .brand-square{width:12px;height:12px}
.brand.lg .brand-name{font-size:11px}
.brand.md .brand-square{width:8px;height:8px}
.brand.md .brand-name{font-size:7.5px}

.hr{position:absolute;height:.6px;background:var(--rule)}
.label{position:absolute;font-size:3.4px;line-height:1.35;text-transform:uppercase}
.re{position:absolute;font-family:"Montserrat",Arial,sans-serif;font-size:5px;letter-spacing:.08em;border-bottom:.5px solid var(--rule);padding-bottom:1px}
.body{position:absolute;font-size:3.3px;line-height:1.5;text-align:justify}
.body p{margin-bottom:3px}
.signature{position:absolute;width:56px;height:12px;background:linear-gradient(90deg,#d9d9d9,#efefef)}
.role{position:absolute;font-size:3.4px}
.contact{position:absolute;display:flex;align-items:center;gap:4px}
.contact .brand{position:static}
.contact-lines{font-size:2.6px;line-height:1.3;border-left:.5px solid currentColor;padding-left:3px}

.band-photo{position:absolute;background:linear-gradient(160deg,var(--sky-a),var(--sky-b) 55%,#0a2440)}
.big-name{position:absolute;left:4px;font-family:"Montserrat",Arial,sans-serif;font-weight:500;font-size:40px;line-height:.95;letter-spacing:.02em}

.cover-title{position:absolute;left:0;right:0;display:flex;justify-content:center;align-items:center;gap:7px}
.cover-title .brand{position:static}
.divider{width:.8px;height:40px;background:currentColor}
.report-title{font-family:"Montserrat",Arial,sans-serif;font-size:9px;letter-spacing:.12em;line-height:1.1}
.meta{position:absolute;font-family:"Montserrat",Arial,sans-serif;font-size:3px;letter-spacing:.06em}
.meta b{font-weight:500}

.invoice-head{position:absolute;left:0;right:0;top:0;height:95px;background:var(--charcoal);color:#fff}
.invoice-foot{position:absolute;left:0;right:0;bottom:0;height:35px;background:var(--charcoal);color:#fff}
.invoice-meta{position:absolute;font-size:3.2px;line-height:1.35}
.inv-table{position:absolute;border-collapse:collapse;font-size:2.8px}
.inv-table td{border-bottom:.5px solid #555;border-left:.4px solid #555;height:6px;padding:0 1px;vertical-align:top}
.inv-table tr:first-child td{border-top:.9px solid #222}
.mist{background:var(--mist)}
</style>
</head>
<body>

<!-- Row 1 -->
<section class="page c1 r1" aria-label="Letterhead, light">
  <div class="brand" style="left:50px;top:38px"><span class="brand-square"></span><span class="brand-name">NORTHFIELD</span></div>
  <div class="hr" style="left:50px;right:30px;top:57px"></div>
  <div class="label" style="left:50px;top:86px">To:<br><br>Name Surname<br>Address Line 1,<br>Address Line 2,<br>City, State, Country,<br>Zip Code</div>
  <div class="re" style="left:50px;right:30px;top:127px">RE: ADD YOUR OWN TITLE</div>
  <div class="body" style="left:50px;right:30px;top:138px">
    <p>Write the opening of your letter here. Keep it short, state the purpose and set out the key points you wish to raise.</p>
    <p>Add supporting detail in this paragraph, such as dates, terms or next steps, and keep the tone clear and direct.</p>
    <p>Close with a brief summary and a note on how the reader can reach you for any follow up.</p>
    <p>Edit all of this text as you please.</p>
  </div>
  <div class="signature" role="img" aria-label="Handwritten signature" style="left:47px;top:244px"></div>
  <div class="role" style="left:50px;top:258px">CEO, Northfield Venture Partners</div>
  <div class="hr" style="left:50px;right:30px;top:298px"></div>
  <div class="contact" style="left:50px;top:303px"><span class="brand"><span class="brand-square"></span></span><div class="contact-lines">Kit Harlow<br>P: +61 400-555-210<br>E: kit@kharlow.co<br>W: northfield.example</div></div>
  <div style="position:absolute;left:162px;top:318px;width:83px;height:25px;background:var(--night)"></div>
</section>

<section class="page c2 r1" aria-label="Cover, light">
  <div class="cover-title" style="top:120px"><span class="brand lg"><span class="brand-square"></span></span><span class="divider"></span><span class="brand lg"><span class="brand-name">NORTHFIELD</span></span></div>
</section>

<section class="page c3 r1 dark" aria-label="Cover, dark">
  <div class="cover-title" style="top:120px"><span class="brand lg"><span class="brand-square"></span></span><span class="divider"></span><span class="brand lg"><span class="brand-name">NORTHFIELD</span></span></div>
</section>

<section class="page c4 r1" aria-label="Letterhead with photo edge">
  <div class="band-photo" role="img" aria-label="Photo of a glass office tower" style="right:0;top:0;width:45px;height:343px"></div>
  <div class="brand" style="left:32px;top:38px"><span class="brand-square"></span><span class="brand-name">NORTHFIELD</span></div>
  <div class="hr" style="left:32px;right:52px;top:57px"></div>
  <div class="label" style="left:32px;top:86px">To:<br><br>Name Surname<br>Address Line 1,<br>Address Line 2,<br>City, State, Country,<br>Zip Code</div>
  <div class="re" style="left:32px;right:52px;top:127px">RE: ADD YOUR OWN TITLE</div>
  <div class="body" style="left:32px;right:52px;top:138px">
    <p>Write the opening of your letter here. Keep it short, state the purpose and set out the key points you wish to raise.</p>
    <p>Add supporting detail in this paragraph, such as dates, terms or next steps, and keep the tone clear and direct.</p>
    <p>Close with a brief summary and a note on how the reader can reach you for any follow up.</p>
    <p>Edit all of this text as you please.</p>
  </div>
  <div class="signature" role="img" aria-label="Handwritten signature" style="left:29px;top:244px"></div>
  <div class="role" style="left:34px;top:258px">CEO, Northfield Venture Partners</div>
  <div class="hr" style="left:32px;right:52px;top:298px"></div>
  <div class="contact" style="left:32px;top:303px"><span class="brand"><span class="brand-square"></span></span><div class="contact-lines">Kit Harlow<br>P: +61 400-555-210<br>E: kit@kharlow.co<br>W: northfield.example</div></div>
</section>

<!-- Row 2 -->
<section class="page c1 r2 mist" aria-label="Letterhead, banded">
  <div style="position:absolute;left:4px;right:0;top:0;height:95px;background:var(--paper)"></div>
  <div style="position:absolute;left:4px;right:0;bottom:0;height:37px;background:var(--paper)"></div>
  <div class="brand md" style="left:50px;top:47px"><span class="brand-square"></span><span class="brand-name">NORTHFIELD</span></div>
  <div class="label" style="left:50px;top:109px">To:<br>Name Surname<br>Address Line 1,<br>Address Line 2,<br>City, State, Country,<br>Zip Code</div>
  <div class="re" style="left:50px;right:30px;top:146px">RE: ADD YOUR OWN TITLE</div>
  <div class="body" style="left:50px;right:30px;top:157px">
    <p>Write the opening of your letter here. Keep it short, state the purpose and set out the key points you wish to raise.</p>
    <p>Add supporting detail in this paragraph, such as dates, terms or next steps, and keep the tone clear and direct.</p>
    <p>Close with a brief summary and a note on how the reader can reach you for any follow up.</p>
    <p>Edit all of this text as you please.</p>
  </div>
  <div class="signature" role="img" aria-label="Handwritten signature" style="left:50px;top:256px"></div>
  <div class="role" style="left:50px;top:270px">CEO, Northfield Venture Partners</div>
  <div class="contact" style="left:50px;top:314px"><span class="brand"><span class="brand-square"></span></span><div class="contact-lines">Kit Harlow<br>P: +61 400-555-210<br>E: kit@kharlow.co<br>W: northfield.example</div></div>
</section>

<section class="page c2 r2" aria-label="Invoice">
  <div class="invoice-head"><div class="brand md" style="left:42px;top:47px"><span class="brand-square"></span><span class="brand-name">NORTHFIELD</span></div></div>
  <div class="invoice-meta" style="left:42px;top:121px">Invoice #:<br>Invoice Date:<br>Customer ID:</div>
  <div class="invoice-meta" style="left:42px;top:139px"><i>Bill To:</i><br><b>Type Name Here</b><br>Shipping Address Line 1<br>Shipping Address Line 2</div>
  <div class="invoice-meta" style="left:111px;top:139px"><i>Ship To:</i><br>Shipping Address Line 1</div>
  <table class="inv-table" style="left:41px;top:164px;width:183px">
    <tr><td>Date</td><td>Your Order #</td><td>Our Order #</td><td>Sales Rep.</td><td>FOB</td><td>Ship Via</td><td>Terms</td><td>Tax ID</td></tr>
    <tr><td></td><td></td><td></td><td></td><td></td><td></td><td></td><td></td></tr>
  </table>
  <table class="inv-table" style="left:41px;top:183px;width:183px">
    <tr><td>Quantity</td><td>Item</td><td>Units</td><td style="width:46px">Description</td><td>Discount %</td><td>Taxable</td><td>Unit Price</td><td>Total</td></tr>
    <tr><td></td><td></td><td></td><td></td><td></td><td></td><td></td><td></td></tr>
    <tr><td></td><td></td><td></td><td></td><td></td><td></td><td></td><td></td></tr>
    <tr><td></td><td></td><td></td><td></td><td></td><td></td><td></td><td></td></tr>
    <tr><td></td><td></td><td></td><td></td><td></td><td></td><td></td><td></td></tr>
    <tr><td></td><td></td><td></td><td></td><td></td><td></td><td></td><td></td></tr>
    <tr><td></td><td></td><td></td><td></td><td></td><td></td><td></td><td></td></tr>
  </table>
  <table class="inv-table" style="left:183px;top:230px;width:41px">
    <tr><td>Subtotal</td><td></td></tr><tr><td>Tax</td><td></td></tr><tr><td>Shipping</td><td></td></tr><tr><td>Misc.</td><td></td></tr><tr><td>Balance</td><td></td></tr>
  </table>
  <div class="invoice-meta" style="left:42px;top:252px">REMITTANCE<br>Customer ID:<br>Date:<br>Amount Due:<br>Amount Enclosed:</div>
  <div class="invoice-foot"><div class="contact" style="left:162px;top:7px"><span class="brand"><span class="brand-square"></span></span><div class="contact-lines">Kit Harlow<br>P: +61 400-555-210<br>E: kit@kharlow.co<br>W: northfield.example</div></div></div>
</section>

<section class="page c3 r2" aria-label="Report cover, light">
  <div class="cover-title" style="top:120px;justify-content:flex-start;padding-left:50px"><span class="brand lg"><span class="brand-square"></span></span><span class="divider"></span><span class="report-title">REPORT COVER<br>LIGHT OPTION</span></div>
  <div class="hr" style="left:50px;right:30px;top:298px"></div>
  <div class="meta" style="left:50px;top:301px"><b>AUG 2021</b> — ENTER OTHER METADATA</div>
  <div class="contact" style="left:158px;top:301px"><span class="brand"><span class="brand-square"></span></span><div class="contact-lines">Kit Harlow<br>P: +61 400-555-210<br>E: kit@kharlow.co<br>W: northfield.example</div></div>
</section>

<section class="page c4 r2 dark" aria-label="Report cover, dark">
  <div class="cover-title" style="top:120px;justify-content:flex-start;padding-left:50px"><span class="brand lg"><span class="brand-square"></span></span><span class="divider"></span><span class="report-title">REPORT COVER<br>DARK OPTION</span></div>
  <div class="hr" style="left:50px;right:30px;top:298px;background:#777"></div>
  <div class="meta" style="left:50px;top:301px"><b>AUG 2021</b> — ENTER OTHER METADATA</div>
  <div class="contact" style="left:158px;top:301px"><span class="brand"><span class="brand-square"></span></span><div class="contact-lines">Kit Harlow<br>P: +61 400-555-210<br>E: kit@kharlow.co<br>W: northfield.example</div></div>
</section>

<!-- Row 3 -->
<section class="page c1 r3" aria-label="Letterhead with side column">
  <div style="position:absolute;left:0;top:0;width:68px;height:343px;background:var(--night)"></div>
  <div class="brand md" style="left:20px;top:34px;color:#fff"><span class="brand-square"></span></div>
  <div class="band-photo" role="img" aria-label="Photo of a glass office tower" style="left:0;top:69px;width:68px;height:175px"></div>
  <div class="contact-lines" style="position:absolute;left:30px;top:260px;color:#fff;transform:rotate(-90deg);transform-origin:left top;top:300px">Kit Harlow<br>P: +61 400-555-210<br>E: kit@kharlow.co<br>W: northfield.example</div>
  <div class="brand" style="left:133px;top:35px"><span class="brand-square"></span><span class="brand-name">NORTHFIELD</span></div>
  <div class="hr" style="left:95px;right:23px;top:66px"></div>
  <div class="label" style="left:95px;top:87px">To:<br><br>Name Surname<br>Address Line 1,<br>Address Line 2,<br>City, State, Country,<br>Zip Code</div>
  <div class="re" style="left:95px;right:23px;top:127px">RE: ADD YOUR OWN TITLE</div>
  <div class="body" style="left:95px;right:23px;top:138px">
    <p>Write the opening of your letter here. Keep it short, state the purpose and set out the key points you wish to raise.</p>
    <p>Add supporting detail in this paragraph, such as dates, terms or next steps, and keep the tone clear and direct.</p>
    <p>Close with a brief summary and a note on how the reader can reach you for any follow up.</p>
    <p>Edit all of this text as you please.</p>
  </div>
  <div class="signature" role="img" aria-label="Handwritten signature" style="left:94px;top:263px"></div>
  <div class="role" style="left:95px;top:277px">CEO, Northfield Venture Partners</div>
</section>

<section class="page c2 r3" aria-label="Brand sheet, light">
  <div class="big-name" style="top:88px">NORTH<br>FIELD</div>
  <div class="brand" style="left:128px;top:310px"><span class="brand-square"></span><span class="brand-name">NORTHFIELD</span></div>
</section>

<section class="page c3 r3 dark" aria-label="Brand sheet, dark">
  <div class="big-name" style="top:88px">NORTH<br>FIELD</div>
  <div class="brand" style="left:128px;top:310px"><span class="brand-square"></span><span class="brand-name">NORTHFIELD</span></div>
</section>

<section class="page c4 r3" aria-label="Letterhead with dark edge">
  <div style="position:absolute;right:0;top:0;width:45px;height:343px;background:#0e0e10"></div>
  <div class="contact-lines" style="position:absolute;left:212px;top:300px;color:#fff;transform:rotate(-90deg);transform-origin:left top">Kit Harlow<br>P: +61 400-555-210<br>E: kit@kharlow.co<br>W: northfield.example</div>
  <div class="brand" style="left:32px;top:46px"><span class="brand-square"></span><span class="brand-name">NORTHFIELD</span></div>
  <div class="hr" style="left:32px;right:52px;top:64px"></div>
  <div class="label" style="left:32px;top:90px">To:<br><br>Name Surname<br>Address Line 1,<br>Address Line 2,<br>City, State, Country,<br>Zip Code</div>
  <div class="re" style="left:32px;right:52px;top:130px">RE: ADD YOUR OWN TITLE</div>
  <div class="body" style="left:32px;right:52px;top:141px">
    <p>Write the opening of your letter here. Keep it short, state the purpose and set out the key points you wish to raise.</p>
    <p>Add supporting detail in this paragraph, such as dates, terms or next steps, and keep the tone clear and direct.</p>
    <p>Close with a brief summary and a note on how the reader can reach you for any follow up.</p>
    <p>Edit all of this text as you please.</p>
  </div>
  <div class="signature" role="img" aria-label="Handwritten signature" style="left:29px;top:250px"></div>
  <div class="role" style="left:34px;top:264px">CEO, Northfield Venture Partners</div>
  <div class="hr" style="left:32px;right:52px;top:318px"></div>
</section>

</body>
</html>
```